Business card templates for our website plus designer opportunity

we require 100 business card designs to start with in the following categories (see below ) please note we require 1000`s of designs in all types of different fields this is just a tester to check the response , we are currently setting up a inkpressly / printory type website/ marketplace we are now looking for freelance designers to make us some default designs to launch the site.

http://www.qorvelto.com/

Brief about qorvelto

we our a manufacture of a large range of products covering many industries we our currently setting up a marketplace where people can buy sell create and find personalized products and custom merchandised very much like printory and mugstacker we are now at the stage of adding content to the site for its launch we our currently looking for some core design templates in fact we need a lot of designs and we are currently looking for high quality designers to join our freelance design team .

The business cards designs

Please note all the text and data on the card can be the same so set up a default template to save yourself time all we really want is the core design front and back please , use inkpressly printory mug stacker for reference or ideas please make sure they are not copied and we have full rights to the any copyright your design may contain , if we pick your designs you we will paid for them asked to make another 200 designs and you will be asked if you would like to join our freelance qorvelto core design team you can always say no its perfectly fine but we have a lot of work to be designed for a lot of different products so there is a good opportunity here to get in before the site goes live in the next few months

Also note the chosen designs must be in vector format as well as jpeg and pdf , any vector files must be created to outlines
once we buy the designs we will own full rights to the copyright of said design and we can change and use these designs in anyway we see fit

Industry: ( 20 number designs for each ) Test run to check response

Agriculture & Farming
Animals & Pet Care
Art & Entertainment
Automotive & Transportation
Beauty & Spa

```html
<!DOCTYPE html>
<html lang="en">
<head>
<meta charset="utf-8">
<title>Qorvelto – Animals &amp; Pet Care Business Card</title>
<link href="https://fonts.googleapis.com/css2?family=Cinzel:wght@400&family=Lato:wght@400;700;900&display=swap" rel="stylesheet">
<style>
  :root {
    --page-bg: #d9d9d9;
    --card-dark: #1f1d1c;
    --card-dark-edge: #2b2928;
    --frame-line: #d8d8d8;
    --text-light: #f2f2f2;
    --text-muted: #cfcfcf;
    --brand-green: #3fae4a;
    --grass-deep: #2f7d1c;
    --grass-mid: #4f9e2a;
    --grass-light: #6fb83a;
  }
  * { margin: 0; padding: 0; box-sizing: border-box; }
  html, body { width: 1200px; height: 900px; overflow: hidden; }
  body {
    background: var(--page-bg);
    font-family: "Lato", sans-serif;
    display: flex;
    flex-direction: column;
    align-items: center;
    justify-content: center;
    gap: 50px;
  }
  .card {
    position: relative;
    width: 630px;
    height: 360px;
    overflow: hidden;
    background: linear-gradient(135deg, var(--card-dark) 0%, var(--card-dark-edge) 60%, var(--card-dark) 100%);
    box-shadow: 0 6px 18px rgba(0,0,0,.25);
  }

  /* Back side */
  .card-back .frame { position: absolute; inset: 0; }
  .card-back .company-name {
    position: absolute;
    top: 150px; left: 0; right: 0;
    text-align: center;
    font-family: "Cinzel", serif;
    font-size: 24px;
    letter-spacing: 1px;
    color: var(--text-light);
  }
  .card-back .website {
    position: absolute;
    bottom: 32px; left: 0; right: 0;
    text-align: center;
    font-family: "Cinzel", serif;
    font-size: 9px;
    letter-spacing: 1px;
    color: var(--text-muted);
  }

  /* Front side */
  .card-front .photo {
    position: absolute;
    top: 0; left: 0; bottom: 0;
    width: 430px;
    background:
      radial-gradient(ellipse at 40% 45%, #f4f4f2 0 22%, transparent 38%),
      linear-gradient(160deg, var(--grass-light), var(--grass-mid) 45%, var(--grass-deep));
    -webkit-mask-image: linear-gradient(90deg, #000 62%, transparent 100%);
    mask-image: linear-gradient(90deg, #000 62%, transparent 100%);
  }
  .brand {
    position: absolute;
    top: 52px; left: 370px;
    text-align: right;
  }
  .brand-name {
    font-weight: 900;
    font-size: 26px;
    letter-spacing: .5px;
    color: var(--brand-green);
    line-height: 1;
  }
  .brand-tagline {
    font-size: 12px;
    color: var(--text-light);
    margin-top: 3px;
  }
  .person {
    position: absolute;
    top: 152px; left: 405px;
    text-align: center;
  }
  .person-name {
    font-size: 17px;
    color: var(--text-light);
    letter-spacing: .3px;
  }
  .person-name .first { color: var(--brand-green); }
  .person-title {
    font-size: 8px;
    font-weight: 700;
    letter-spacing: 1px;
    color: var(--text-light);
    margin-top: 1px;
  }
  .contact {
    position: absolute;
    display: flex;
    align-items: flex-end;
    gap: 10px;
    color: var(--text-light);
    font-size: 12px;
    line-height: 1.3;
  }
  .contact svg { flex: none; fill: none; stroke: var(--text-light); stroke-width: 1.6; }
  .contact-web { top: 232px; left: 430px; }
  .contact-phone { top: 276px; left: 285px; }
  .contact-address { top: 300px; left: 100px; }
</style>
</head>
<body>

  <section class="card card-back">
    <svg class="frame" width="630" height="360" viewBox="0 0 630 360">
      <polyline points="190,326 28,326 28,28 602,28 602,326 470,326" fill="none" stroke="var(--frame-line)" stroke-width="1.4"/>
    </svg>
    <h1 class="company-name">Company Name</h1>
    <p class="website">www.qorvelto.com</p>
  </section>

  <section class="card card-front">
    <div class="photo" role="img" aria-label="Photo of a small white fluffy dog standing on green grass"></div>

    <div class="brand">
      <p class="brand-name">QORVELTO</p>
      <p class="brand-tagline">Animals &amp; Pet Care</p>
    </div>

    <div class="person">
      <p class="person-name"><span class="first">DANIEL</span> HARROW</p>
      <p class="person-title">PRESIDENT</p>
    </div>

    <div class="contact contact-web">
      <svg width="20" height="20" viewBox="0 0 20 20" aria-hidden="true">
        <circle cx="10" cy="10" r="8.5"/>
        <ellipse cx="10" cy="10" rx="3.8" ry="8.5"/>
        <line x1="1.5" y1="10" x2="18.5" y2="10"/>
        <line x1="3" y1="5.5" x2="17" y2="5.5"/>
        <line x1="3" y1="14.5" x2="17" y2="14.5"/>
      </svg>
      <p>contact@qorvelto.com<br>www.qorvelto.com</p>
    </div>

    <div class="contact contact-phone">
      <svg width="18" height="18" viewBox="0 0 18 18" aria-hidden="true">
        <path d="M4 1.5l3 3.5-1.6 2a9 9 0 0 0 5.6 5.6l2-1.6 3.5 3-1.8 2.3C8 15.5 2.5 10 1.7 3.3z" fill="var(--text-light)" stroke="none"/>
      </svg>
      <p>555 014 2287<br>555 019 3364</p>
    </div>

    <div class="contact contact-address">
      <svg width="20" height="18" viewBox="0 0 20 18" aria-hidden="true">
        <path d="M10 1.5L1.5 9h2.5v7.5h4.5v-5h3v5h4.5V9h2.5z" fill="var(--text-light)" stroke="none"/>
      </svg>
      <p>418 Meadowlark Ave.<br>Brookhaven, IL 60412</p>
    </div>
  </section>

</body>
</html>
```